Professional Services (B-2-B) Business Cards (Front & Back)

Corvantis is a business-to-business professional services company in the legal sector. They typically present to c-suite and executive functions who are looking for providers with expertise, and experience. Our business card should look and feel professional and contemporary, but we are not a startup tech company, so we want the tone to be more mature.

```html
<!DOCTYPE html>
<html lang="en">
<head>
<meta charset="utf-8">
<title>Corvantis Business Card — Front &amp; Back</title>
<link href="https://fonts.googleapis.com/css2?family=Montserrat:wght@400;500;700&display=swap" rel="stylesheet">
<style>
  :root {
    --stage: #e6e6e4;
    --paper: #fbfbfa;
    --navy: #2c3a82;
    --navy-deep: #27347a;
    --ink-grey: #7d7d7d;
    --white: #ffffff;
  }
  * { box-sizing: border-box; margin: 0; padding: 0; }
  html, body {
    width: 1200px; height: 801px; overflow: hidden;
    background: var(--stage);
    font-family: "Montserrat", Arial, sans-serif;
  }
  .stage {
    position: relative; width: 1200px; height: 801px;
  }
  .card {
    position: absolute; top: 252px;
    width: 520px; height: 297px;
    box-shadow: 0 8px 22px rgba(0,0,0,0.16);
    overflow: hidden;
  }
  .card--front { left: 50px; background: var(--paper); }
  .card--back { left: 630px; background: var(--navy); }

  /* Front */
  .brand {
    position: absolute; left: 34px; top: 108px;
    display: flex; align-items: center; gap: 16px;
  }
  .brand__square {
    width: 30px; height: 30px; background: var(--navy);
  }
  .brand__name {
    font-size: 27px; font-weight: 400; letter-spacing: 9px;
    color: var(--ink-grey); text-transform: uppercase;
  }
  .person {
    position: absolute; left: 34px; top: 200px;
  }
  .person__name {
    font-size: 15px; font-weight: 700; color: var(--navy);
    letter-spacing: 0.5px; text-transform: uppercase;
  }
  .person__title {
    font-size: 12px; color: var(--ink-grey); margin-top: 2px;
  }
  .contacts {
    position: absolute; top: 248px; left: 34px; right: 34px;
    display: flex; justify-content: space-between;
  }
  .contacts__group { display: flex; flex-direction: column; gap: 4px; }
  .contact {
    display: flex; align-items: center; gap: 8px;
    font-size: 12px; color: var(--ink-grey); letter-spacing: 0.3px;
  }
  .contact__icon { width: 13px; height: 13px; flex: none; }
  .contacts__group--online { margin-top: -58px; }

  /* Back */
  .back__field {
    position: absolute; inset: 0;
    background: linear-gradient(160deg, var(--navy) 0%, var(--navy-deep) 100%);
  }
  .back__brand {
    position: absolute; right: 70px; top: 132px;
    font-size: 18px; font-weight: 500; letter-spacing: 5px;
    color: var(--white); text-transform: uppercase;
  }
</style>
</head>
<body>
<main class="stage">

  <section class="card card--front" aria-label="Card front">
    <div class="brand">
      <span class="brand__square"></span>
      <span class="brand__name">Corvantis</span>
    </div>

    <div class="person">
      <p class="person__name">Mara Ellison</p>
      <p class="person__title">President &amp; CEO</p>
    </div>

    <div class="contacts">
      <div class="contacts__group">
        <p class="contact">
          <svg class="contact__icon" viewBox="0 0 14 14" aria-hidden="true">
            <circle cx="7" cy="7" r="7" fill="var(--navy)"/>
            <path d="M4.3 3.6c.4-.3.8-.2 1 .2l.6 1.1c.2.4.1.7-.2.9l-.4.3c.3.8 1 1.6 1.9 2l.3-.4c.2-.3.6-.4.9-.2l1.1.6c.4.2.5.6.2 1-.6.8-1.4 1-2.4.5C5.5 8.9 4.4 7.8 3.8 6c-.3-1 0-1.8.5-2.4z" fill="var(--white)"/>
          </svg>
          (415) 555 - 0142
        </p>
        <p class="contact">
          <svg class="contact__icon" viewBox="0 0 14 14" aria-hidden="true">
            <circle cx="7" cy="7" r="7" fill="var(--navy)"/>
            <rect x="4.8" y="3.2" width="4.4" height="7.6" rx="0.8" fill="none" stroke="var(--white)" stroke-width="1"/>
          </svg>
          (203) 555 - 0187
        </p>
      </div>
      <div class="contacts__group contacts__group--online">
        <p class="contact">
          <svg class="contact__icon" viewBox="0 0 14 14" aria-hidden="true">
            <circle cx="7" cy="7" r="7" fill="var(--navy)"/>
            <rect x="3.5" y="4.5" width="7" height="5" fill="none" stroke="var(--white)" stroke-width="0.9"/>
            <path d="M3.5 4.5 7 7.3l3.5-2.8" fill="none" stroke="var(--white)" stroke-width="0.9"/>
          </svg>
          mellison@corvantis.tech
        </p>
        <p class="contact">
          <svg class="contact__icon" viewBox="0 0 14 14" aria-hidden="true">
            <circle cx="7" cy="7" r="7" fill="var(--navy)"/>
            <circle cx="7" cy="7" r="3.6" fill="none" stroke="var(--white)" stroke-width="0.9"/>
            <path d="M3.4 7h7.2M7 3.4c-1.6 2-1.6 5.2 0 7.2M7 3.4c1.6 2 1.6 5.2 0 7.2" fill="none" stroke="var(--white)" stroke-width="0.8"/>
          </svg>
          www.corvantis.tech
        </p>
      </div>
    </div>
  </section>

  <section class="card card--back" aria-label="Card back">
    <div class="back__field" role="img" aria-label="Deep navy field with a subtle tone-on-tone embossed pattern"></div>
    <span class="back__brand">Corvantis</span>
  </section>

</main>
</body>
</html>
```